Vornel Estates - Chat n’ Cheer Thursday Graphic Invite

We need a graphic design for a corporate reception that we are calling Chat n’ Cheer Thursday. The invite should read:

"QBR invites you to join us at Chat n’ Cheer Thursday

Monday, Jan 22nd
6:30 - 8:30 pm EST

Copper Ladle - Lounge Room

48210 E Pelican Grove Rd
Marlowe Bay, FL 33290

Join us for excellent wine and tasty bites at our semi-annual DAW reception. Swing by whenever you can – timing is casual and we'd love to see you there!"

Please feel free to use fun photos from the Copper Ladle gallery: https://www.copperladlegrill.com/photos

Also, please use the QBR logo attached.

Target Market(s)

Corporate professional

Colors
0054AA
0677BA
7BADD7
CADEEF
E8F1F8

Requirements
Must have
• QBR logo, attached verbiage

```html
<!DOCTYPE html>
<html lang="en">
<head>
<meta charset="utf-8">
<title>Chat n’ Cheer Thursday Invitation</title>
<link rel="stylesheet" href="https://fonts.googleapis.com/css2?family=Great+Vibes&family=Gilda+Display&family=Inter+Tight:wght@300;400;700&display=swap">
<style>
  :root {
    --ink-white: #ffffff;
    --ink-soft: rgba(255,255,255,0.92);
    --night: #14110f;
    --night-mid: #221b17;
    --wall-warm: #3a2a20;
    --floor-amber: #6b3a1c;
    --glass-cool: #2f3a3e;
    --pill-line: rgba(255,255,255,0.85);
  }
  * { margin: 0; padding: 0; box-sizing: border-box; }
  html, body { width: 933px; height: 1200px; overflow: hidden; background: var(--night); }
  .invite {
    position: relative;
    width: 933px;
    height: 1200px;
    overflow: hidden;
    color: var(--ink-white);
    font-family: "Inter Tight", Arial, sans-serif;
  }
  .venue-photo {
    position: absolute;
    inset: 0;
    background:
      radial-gradient(ellipse 380px 520px at 840px 520px, var(--glass-cool) 0%, transparent 70%),
      radial-gradient(ellipse 700px 320px at 640px 1150px, var(--floor-amber) 0%, transparent 75%),
      linear-gradient(180deg, var(--night) 0%, var(--night-mid) 45%, var(--wall-warm) 80%, #4a2a16 100%);
  }
  .venue-shade {
    position: absolute;
    inset: 0;
    background: linear-gradient(90deg, rgba(10,8,7,0.55) 0%, rgba(10,8,7,0.25) 55%, rgba(10,8,7,0) 100%);
  }
  .brand {
    position: absolute;
    top: 110px;
    left: 0;
    width: 100%;
    display: flex;
    justify-content: center;
    align-items: center;
    gap: 12px;
  }
  .brand-mark {
    width: 24px;
    height: 24px;
    background: var(--ink-white);
  }
  .brand-name {
    font-weight: 700;
    font-size: 42px;
    letter-spacing: 2px;
    color: var(--ink-white);
  }
  .lead-in {
    position: absolute;
    top: 213px;
    left: 0;
    width: 100%;
    text-align: center;
    font-weight: 400;
    font-size: 19px;
    letter-spacing: 5.5px;
    padding-left: 20px;
  }
  .event-title {
    position: absolute;
    top: 250px;
    left: 0;
    width: 100%;
    text-align: center;
    font-family: "Great Vibes", cursive;
    font-weight: 400;
    font-size: 88px;
    line-height: 1.1;
    padding-left: 10px;
    white-space: nowrap;
  }
  .event-date {
    position: absolute;
    top: 441px;
    left: 94px;
    font-family: "Gilda Display", Georgia, serif;
    font-size: 35px;
    line-height: 1;
    white-space: nowrap;
  }
  .event-time {
    position: absolute;
    top: 486px;
    left: 96px;
    font-family: "Gilda Display", Georgia, serif;
    font-size: 25px;
    letter-spacing: 2px;
    white-space: nowrap;
  }
  .event-note {
    position: absolute;
    top: 612px;
    left: 100px;
    width: 360px;
    font-size: 23px;
    line-height: 35.5px;
    font-weight: 300;
    color: var(--ink-soft);
    white-space: nowrap;
  }
  .event-note strong { font-weight: 700; color: var(--ink-white); }
  .venue-name {
    position: absolute;
    top: 927px;
    left: 104px;
    font-weight: 700;
    font-size: 21.5px;
    letter-spacing: -0.4px;
    white-space: nowrap;
  }
  .venue-address {
    position: absolute;
    top: 986px;
    left: 92px;
    width: 344px;
    height: 72px;
    border: 1px solid var(--pill-line);
    border-radius: 36px;
    padding: 11px 0 0 38px;
    font-size: 20px;
    line-height: 24px;
    letter-spacing: -0.5px;
    font-style: normal;
    white-space: nowrap;
  }
</style>
</head>
<body>
  <main class="invite">
    <div class="venue-photo" role="img" aria-label="Dimly lit private lounge room with a long set dining table, upholstered chairs, a glass wall wine rack and warm wooden parquet floor"></div>
    <div class="venue-shade"></div>

    <header class="brand">
      <span class="brand-mark"></span>
      <span class="brand-name">QBR</span>
    </header>

    <p class="lead-in">INVITES YOU TO JOIN US AT</p>
    <h1 class="event-title">Chat n’ Cheer Thursday</h1>

    <p class="event-date">MONDAY, JAN 22ND</p>
    <p class="event-time">6:30 - 8:30 PM EST</p>

    <p class="event-note"><strong>Join us for excellent wine<br>and tasty bites</strong> at our<br>semi-annual DAW reception.<br>Swing by whenever you can<br>– timing is casual and we'd<br>love to see you there!</p>

    <p class="venue-name">Copper Ladle - Lounge Room</p>
    <address class="venue-address">48210 E Pelican Grove Rd<br>Marlowe Bay, FL 33290</address>
  </main>
</body>
</html>
```